Bluvekko Flyer

Here is the original design of a double sided flyer that we are going to use to mail out. But this one looks too cluttered right now and we want it to match our website more (www.bluvekko-example.com). I will send over the logo attachment as well.

```html
<!DOCTYPE html>
<html lang="en">
<head>
<meta charset="utf-8">
<title>Bluvekko Flyer</title>
<link rel="stylesheet" href="https://fonts.googleapis.com/css2?family=Questrial&family=Arimo:ital,wght@0,400;0,700;1,700&display=swap">
<style>
  :root {
    --green: #6cc04a;
    --ink: #2b2b2b;
    --grey: #6d6e71;
    --strip: #8c8c8e;
    --panel: #232323;
    --paper: #ffffff;
  }
  * { margin: 0; padding: 0; box-sizing: border-box; }
  html, body { width: 1200px; height: 800px; overflow: hidden; background: var(--paper); }
  .flyer {
    position: relative;
    width: 1200px;
    height: 800px;
    background: var(--paper);
    font-family: "Questrial", "Century Gothic", sans-serif;
    color: var(--ink);
  }
  .edge-strip { position: absolute; left: 0; top: 0; width: 86px; height: 800px; background: var(--strip); }

  .brand { position: absolute; left: 119px; top: 58px; }
  .brand-row { display: flex; align-items: center; gap: 16px; }
  .brand-name {
    font-family: "Questrial", "Century Gothic", sans-serif;
    font-size: 80px; line-height: 1; letter-spacing: 1px; color: var(--grey);
  }
  .brand-dot { width: 54px; height: 54px; border-radius: 50%; background: var(--green); }
  .brand-tagline { margin-top: 6px; font-size: 22px; color: var(--grey); }

  .postage-box {
    position: absolute; left: 1015px; top: 37px; width: 132px; height: 144px;
    border: 2px solid var(--ink);
    display: flex; align-items: center; justify-content: center;
    font-family: "Arimo", Arial, sans-serif; font-size: 22px;
  }

  .headline {
    position: absolute; left: 106px; top: 184px; width: 1056px;
    text-align: center; font-size: 41px; color: var(--green); white-space: nowrap;
  }
  .rule { position: absolute; height: 3px; background: var(--green); }
  .rule-top { left: 106px; top: 240px; width: 1056px; }
  .rule-bottom { left: 106px; top: 687px; width: 611px; }

  .section-title {
    position: absolute; width: 480px; text-align: center;
    font-family: "Arimo", Arial, sans-serif; font-weight: 700;
    font-size: 28px; color: var(--grey);
  }
  .solutions-title { left: 95px; top: 280px; }
  .anywhere-title { left: 95px; top: 475px; }

  .solutions-copy {
    position: absolute; left: 115px; top: 333px; width: 440px;
    text-align: center; font-family: "Arimo", Arial, sans-serif;
    font-size: 20px; line-height: 23px;
  }

  .service-panel {
    position: absolute; left: 752px; top: 306px; width: 414px; height: 122px;
    background: var(--panel);
  }

  .venue-list {
    position: absolute; left: 148px; top: 530px; width: 460px;
    display: grid; grid-template-columns: 234px 226px; row-gap: 24px;
    list-style: none; font-family: "Arimo", Arial, sans-serif; font-size: 21px;
  }
  .venue-list li { position: relative; padding-left: 48px; line-height: 24px; }
  .venue-list li::before {
    content: ""; position: absolute; left: 8px; top: 8px;
    width: 8px; height: 8px; border-radius: 50%; background: var(--ink);
  }

  .contact {
    position: absolute; left: 114px; top: 702px;
    font-family: "Arimo", Arial, sans-serif; font-weight: 700; font-style: italic;
    font-size: 23px; line-height: 30px; color: var(--green);
  }

  .address-box {
    position: absolute; left: 746px; top: 480px; width: 401px; height: 272px;
    border: 3px solid var(--green);
    display: flex; flex-direction: column; align-items: center; justify-content: center;
    gap: 16px; font-family: "Arimo", Arial, sans-serif; font-size: 22px;
  }
</style>
</head>
<body>
  <main class="flyer">
    <div class="edge-strip"></div>

    <header class="brand">
      <div class="brand-row">
        <span class="brand-name">BLUVEKKO</span>
        <span class="brand-dot"></span>
      </div>
      <p class="brand-tagline">Tenant updates and news</p>
    </header>

    <div class="postage-box">Postage</div>

    <h1 class="headline">Simplifying Communications Between Buildings &amp; Tenants</h1>
    <div class="rule rule-top"></div>

    <h2 class="section-title solutions-title">Bluvekko’s Powerful Solutions</h2>
    <p class="solutions-copy">Bluvekko enabled buildings provide managers the opportunity to notify residents of new and existing services at home or on the go.</p>

    <div class="service-panel" role="img" aria-label="Illustration: broadcast signal icon with an arrow pointing to a person figure"></div>

    <h2 class="section-title anywhere-title">Use Bluvekko Anywhere</h2>
    <ul class="venue-list">
      <li>Apartments</li>
      <li>Stadiums</li>
      <li>Hotels</li>
      <li>Churches</li>
      <li>Colleges</li>
      <li>Offices</li>
    </ul>

    <div class="rule rule-bottom"></div>
    <p class="contact">Call a Bluvekko Representative at: (555) 014-2286<br>Or visit us at: www.bluvekko-example.com</p>

    <div class="address-box">
      <span class="recipient-name">Alex Rowan</span>
      <span class="recipient-address">Address</span>
    </div>
  </main>
</body>
</html>
```